Book cover for a New Adult, romance/ contemporary novel.

I need a full front, back, and spine cover for my upcoming book. The novel is a romance/ coming of age book and is similar to Every Quiet Harbor by Marisol Pekkar. My main audience is women in their late teens/ early 20's. The book is an emotional, reminiscent piece and I would love to see some cover designs with a darker palette like Waiting on Tuesday, Nine Rooms Away, or Lucian and Omar (but I also adore some lighter covers, especially those that feature the couple such as Any Given Then or Until Each Dawn). Feel free to send some minimal designs as well if you have any! A great idea of that would be the cover for Salt and Clover or Waiting on Tuesday. If you go with a minimal design, I'd love to see silhouettes or maybe a burning candle. Another possible idea I thought of would be a scene at a concert with the crowd silhouetted and then my main character (more details on her below) standing in the middle of it all. I prefer animation/drawing etc over real models. But feel free to send me whatever you think might match the vibe, I'd love to see anything you have in mind! Some main symbols in my book are stars and candles. The main character (Hana) is a female Korean with brown, medium length straight hair, and the love interest (Theo) is a tall and thin male Caucasian with curly brown hair. The book is openly emotional, wistful, and sets an ache in your chest, so I can't wait to see what designs you artists come up with! (My barcode will need to be included on the back cover, and I am getting that soon!)
The title is "A Map Toward Dusk" and the author's name is Brynn Okafor. The book's dimensions will be 5.5x8.25. The blurb for the back cover is:
When happily ever falls apart, all you can do is move forward… and reminisce. Hana Yoon returns home from college following a tragic incident she can’t bring herself to talk about and a breakup with her boyfriend, Theo Marchetti. Finding it difficult to confront her traumas, she begins therapy. Hana takes the therapist on a rollercoaster journey of her college life, retelling the events that caused her relationship to spiral out of control and led to her dropping out of pre-med despite that being her life-long dream. Hana sets out to remember how things were before everything got so messed up, and figure out how to continue living now that they are.
The author bio for the back cover is:
Brynn Okafor is the author of A Restless Hour. She is a self published writer from Las Vegas who likes to pretend she’s currently in a New York bookstore, drinking a latte, while listening to a carefully curated playlist. When she’s not writing, Brynn is taking care of her plant babies and cuddling with the cutest puppy in the world.

```html
<!DOCTYPE html>
<html lang="en">
<head>
<meta charset="utf-8">
<title>A Map Toward Dusk — Full Cover</title>
<link rel="stylesheet" href="https://fonts.googleapis.com/css2?family=Cormorant+Garamond:wght@500&family=Playfair+Display:ital,wght@0,400;1,400;1,700&family=Sue+Ellen+Francisco&display=swap">
<style>
  :root {
    --paper: #ffffff;
    --ink: #11100e;
    --gold: #a07832;
    --gold-line: #c9a865;
    --cream: #f4f1ea;
    --muted: #9a9893;
    --avatar: #e6e6e8;
    --glow: #c98a2e;
  }
  * { box-sizing: border-box; margin: 0; padding: 0; }
  html, body {
    width: 1200px; height: 864px; overflow: hidden;
    background: var(--paper);
  }
  .cover {
    position: absolute; left: 30px; top: 32px;
    width: 1140px; height: 800px;
    display: flex;
  }
  .back {
    width: 534px; height: 100%;
    background: var(--ink);
    position: relative;
    color: var(--cream);
  }
  .back-heading {
    position: absolute; top: 240px; left: 0; width: 100%;
    text-align: center;
    font-family: "Playfair Display", serif;
    font-size: 17px; letter-spacing: 2.5px;
    color: var(--cream);
  }
  .back-rule {
    position: absolute; top: 271px; left: 241px;
    width: 53px; height: 1px; background: var(--muted);
  }
  .author-bio {
    position: absolute; top: 302px; left: 142px; width: 300px;
    text-align: center;
    font-family: "Playfair Display", serif; font-style: italic;
    font-size: 13.2px; line-height: 21.6px;
    color: var(--cream);
  }
  .author-bio strong { font-weight: 700; }
  .author-photo {
    position: absolute; left: 190px; top: 464px;
    width: 139px; height: 139px; border-radius: 50%;
    background: var(--avatar);
    border: 3px solid var(--cream);
  }
  .spine {
    width: 73px; height: 100%;
    background: var(--gold);
    position: relative;
    border-right: 1px solid var(--gold-line);
  }
  .spine-author {
    position: absolute; top: 88px; left: 26px;
    writing-mode: vertical-rl;
    font-family: "Cormorant Garamond", serif; font-weight: 500;
    font-size: 15px; letter-spacing: 6px;
    color: var(--ink);
  }
  .spine-title {
    position: absolute; top: 432px; left: 12px;
    writing-mode: vertical-rl;
    font-family: "Sue Ellen Francisco", cursive;
    font-size: 46px; line-height: 1; white-space: nowrap;
    color: var(--cream);
  }
  .front {
    flex: 1; height: 100%;
    background: var(--gold);
    position: relative; overflow: hidden;
  }
  .silhouette-art {
    position: absolute; left: 38px; top: 330px;
    width: 466px; height: 480px;
    border-radius: 46% 46% 0 0 / 38% 38% 0 0;
    background: radial-gradient(ellipse 90px 110px at 55% 88%, var(--glow) 0%, #5a3a12 35%, var(--ink) 75%);
  }
  .front-author {
    position: absolute; top: 78px; left: 0; width: 100%;
    text-align: center;
    font-family: "Cormorant Garamond", serif; font-weight: 500;
    font-size: 26px; letter-spacing: 9px;
    color: var(--ink);
    padding-left: 12px;
  }
  .front-title {
    position: absolute; top: 210px; left: 0; width: 100%;
    text-align: center;
    font-family: "Sue Ellen Francisco", cursive;
    font-size: 100px; line-height: 118px;
    color: var(--cream);
    padding-left: 20px;
  }
  .front-title span { display: block; }
</style>
</head>
<body>
  <main class="cover">
    <section class="back">
      <h2 class="back-heading">About the Author</h2>
      <div class="back-rule"></div>
      <p class="author-bio"><strong>Brynn Okafor</strong> is the author of A Restless Hour. She is a self published writer from Las Vegas who likes to pretend she’s currently in a New York bookstore, drinking a latte, while listening to a carefully curated playlist. When she’s not writing, Brynn is taking care of her plant babies and cuddling with the cutest puppy in the world.</p>
      <div class="author-photo" role="img" aria-label="Author portrait placeholder"></div>
    </section>
    <section class="spine">
      <div class="spine-author">BRYNN OKAFOR</div>
      <div class="spine-title">A Map Toward Dusk</div>
    </section>
    <section class="front">
      <div class="silhouette-art" role="img" aria-label="Silhouettes of two faces back to back with a lit candle glowing below"></div>
      <div class="front-author">BRYNN OKAFOR</div>
      <h1 class="front-title"><span>A Map</span><span>Toward</span><span>Dusk</span></h1>
    </section>
  </main>
</body>
</html>
```